Merchandising für Schülermarketing
Zielgruppe
VANTOL Lager & Markt gibt es bereits seit 1964. Die VANTOL Lager & Markt Deutschland GmbH zählt national und international zu den Marktführern im Großhandel und betreibt mit den Marken VANTOL und L+M BRIKENDO 107 Cash & Carry Märkte in Deutschland mit mehr als 17.000 Mitarbeitern. Wir haben 50.000 Artikel im Sortiment und bedienen damit Kunden aus Gastronomie, Hotellerie, Kiosken, Tankstellen, Vereinen, Freiberuflern, etc.
Für unsere Ausbildungsberufe in den Großmärkten (insbes. Kaufmann im Groß- und Außenhandel, Verkäufer, Einzelhandelskaufmann, Fachkraft für Lagerlogistik) suchen wir deutschlandweit viele Azubis. Zielgruppe sind Schüler mit mind. Realschulabschluss.
Aufgabenstellung
Deutschlandweit nehmen wir für das Azubimarketing auf verschiedenen Recruitingmessen teil. Dort verteilen wir Infomaterial aber auch Giveaways. Die Giveaways aktualisieren wir derzeit (Kulis, Textmarker in blau & gelb, faltbarer Einkaufsbeutel mit Logo). Neu dazu soll ein Jutebeutel für die Zielgruppe Schüler kommen, für den wir ein Design suchen.
Der Beutel soll das aktuelle Firmenlogo sichtbar tragen, aber dennoch optisch für die junge Zielgruppe ansprechend sein, so dass er regelmäßig genutzt wird. Gern kann das Design einen grafischen Aufdruck beinhalten oder einen witzigen Spruch, der irgendwie mit Arbeiten bei Vantol in Zusammenhang steht.

```html
<!DOCTYPE html>
<html lang="de">
<head>
<meta charset="utf-8">
<title>Juter Stoff – Jutebeutel</title>
<link rel="stylesheet" href="https://fonts.googleapis.com/css2?family=Kaushan+Script&family=Norican&display=swap">
<style>
  :root {
    --ink: #111111;
    --paper: #ffffff;
    --rule: #9a9a9a;
  }
  * { margin: 0; padding: 0; box-sizing: border-box; }
  html, body {
    width: 815px;
    height: 1200px;
    overflow: hidden;
    background: var(--paper);
  }
  .bag-print {
    position: relative;
    width: 815px;
    height: 1200px;
    background: var(--paper);
    color: var(--ink);
  }
  .slogan {
    position: absolute;
    left: 0;
    top: 0;
    width: 815px;
    height: 700px;
    font-family: "Kaushan Script", cursive;
    font-weight: 400;
    line-height: 1;
  }
  .slogan__line {
    position: absolute;
    white-space: nowrap;
    transform-origin: left bottom;
  }
  .slogan__line--first {
    left: 52px;
    top: 360px;
    font-size: 142px;
    transform: rotate(-15deg);
  }
  .slogan__line--second {
    left: 178px;
    top: 455px;
    font-size: 150px;
    letter-spacing: 6px;
    transform: rotate(-12deg);
  }
  .signoff {
    position: absolute;
    left: 0;
    top: 940px;
    width: 815px;
    text-align: center;
  }
  .signoff__lead {
    font-family: "Norican", cursive;
    font-size: 60px;
    line-height: 1;
  }
  .signoff__brand {
    margin-top: 4px;
    display: flex;
    align-items: center;
    justify-content: center;
    gap: 18px;
    font-family: "Kaushan Script", cursive;
    font-size: 100px;
    line-height: 1.1;
    color: var(--ink);
  }
  .signoff__brand-mark {
    width: 26px;
    height: 26px;
    background: var(--ink);
  }
  .signoff__since {
    margin: 4px auto 0;
    width: 420px;
    display: flex;
    align-items: center;
    gap: 10px;
    font-family: "Norican", cursive;
    font-size: 40px;
    line-height: 1;
  }
  .signoff__since::before,
  .signoff__since::after {
    content: "";
    flex: 1;
    height: 1px;
    background: var(--rule);
  }
</style>
</head>
<body>
  <main class="bag-print">
    <h1 class="slogan">
      <span class="slogan__line slogan__line--first">JUTER</span>
      <span class="slogan__line slogan__line--second">STOFF!</span>
    </h1>
    <footer class="signoff">
      <p class="signoff__lead">mehr davon bei</p>
      <p class="signoff__brand"><span class="signoff__brand-mark" aria-hidden="true"></span>VANTOL</p>
      <p class="signoff__since">established 1964</p>
    </footer>
  </main>
</body>
</html>
```